Local business providing residential house cleaning services

We need a business card design that is "cute" or "cartoonish" while still maintaining a professional appeal. Tidy Lark Cleaners is the name. We would like to use a "pin up girl" or maid next to the name with a broom or vacuum cleaner. We want the look to have a 50's American look to it. We are not sure if we want the pin up girl in a maid outfit or with a broom or vacuum cleaner but we hope some of you will be able to take these ideas and be creative. If you have any questions at all please don't hesitate to message me so that we can get the best design possible. Thank you very much and I look forward to seeing some designs! Mona Pritchett

Target Market(s)

Upper class Americans that are busy and have money and want to come home to a clean house.

Industry/Entity Type

Cleaning Service

Contact Information for Business Card

Pin up girl incorporated into the card is a must.

Font styles to use
Decorative
Script

Requirements
Must have
• Pin up girl
Nice to have
• A crown used on the Q possibly.

```html
<!DOCTYPE html>
<html lang="en">
<head>
<meta charset="utf-8">
<title>Tidy Lark Cleaners – Business Card</title>
<link rel="stylesheet" href="https://fonts.googleapis.com/css2?family=Great+Vibes&family=Parisienne&family=Didact+Gothic&display=swap">
<style>
  :root {
    --backdrop: #e9b39f;
    --card-black: #141414;
    --paper: #dcdad6;
    --paper-stripe: #cfcdc9;
    --ink: #1b1b1b;
    --ink-soft: #3a3a3a;
    --dot: #f2f2f2;
    --art-top: #2a2a2a;
    --art-mid: #b8b2aa;
    --art-gold: #c9a24a;
  }
  * { box-sizing: border-box; margin: 0; padding: 0; }
  html, body {
    width: 1200px;
    height: 960px;
    overflow: hidden;
    background: var(--backdrop);
  }
  .sheet {
    width: 1200px;
    height: 960px;
    display: flex;
    flex-direction: column;
    align-items: center;
    justify-content: center;
    gap: 40px;
  }
  .card {
    position: relative;
    width: 700px;
    height: 400px;
    background: var(--card-black);
    box-shadow: 0 10px 26px rgba(90, 40, 25, 0.28);
  }

  /* Front */
  .card-front { padding: 18px; }
  .front-panel {
    position: relative;
    width: 100%;
    height: 100%;
    background: var(--paper);
    outline: 3px dotted var(--dot);
    outline-offset: -0px;
    box-shadow: 0 0 0 8px var(--card-black);
  }
  .front-frame {
    position: absolute;
    inset: 6px;
    border: 3px dotted var(--dot);
    pointer-events: none;
  }
  .front-panel { outline: none; box-shadow: none; background: var(--card-black); }
  .front-paper {
    position: absolute;
    inset: 18px;
    background: var(--paper);
  }
  .front-figure {
    position: absolute;
    left: 40px;
    top: 28px;
    width: 150px;
    height: 290px;
    border-radius: 70px 70px 20px 20px;
    background: linear-gradient(180deg, var(--art-top) 0%, var(--art-top) 40%, var(--art-mid) 70%, var(--art-mid) 100%);
  }
  .front-logo {
    position: absolute;
    left: 210px;
    top: 88px;
    font-family: "Great Vibes", cursive;
    font-weight: 400;
    font-size: 76px;
    line-height: 0.95;
    color: var(--ink);
  }

  /* Back */
  .card-back {
    background: var(--card-black);
    padding: 0 0 44px 0;
  }
  .back-paper {
    position: relative;
    width: 100%;
    height: 100%;
    background: repeating-linear-gradient(90deg,
      var(--paper) 0px, var(--paper) 42px,
      var(--paper-stripe) 42px, var(--paper-stripe) 84px);
  }
  .back-logo {
    position: absolute;
    left: 60px;
    top: 48px;
    font-family: "Great Vibes", cursive;
    font-weight: 400;
    font-size: 44px;
    line-height: 0.9;
    color: var(--ink);
  }
  .contact-name {
    position: absolute;
    left: 60px;
    top: 176px;
    font-family: "Parisienne", cursive;
    font-size: 34px;
    color: var(--ink);
  }
  .contact-lines {
    position: absolute;
    left: 60px;
    top: 262px;
    font-family: "Didact Gothic", sans-serif;
    color: var(--ink-soft);
  }
  .contact-phone { font-size: 24px; letter-spacing: 0.5px; }
  .contact-email { font-size: 17px; }
  .back-figure {
    position: absolute;
    right: 40px;
    top: 20px;
    width: 200px;
    height: 336px;
    border-radius: 80px 80px 10px 10px;
    background: linear-gradient(180deg, var(--art-top) 0%, var(--art-top) 45%, var(--art-mid) 72%, var(--art-gold) 100%);
  }
</style>
</head>
<body>
<main class="sheet">
  <section class="card card-front" aria-label="Card front">
    <div class="front-panel">
      <div class="front-frame"></div>
      <div class="front-paper">
        <div class="front-figure" role="img" aria-label="Illustration of a 1950s pin-up maid holding a feather duster"></div>
        <p class="front-logo">Tidy Lark<br>Cleaners</p>
      </div>
    </div>
  </section>

  <section class="card card-back" aria-label="Card back">
    <div class="back-paper">
      <p class="back-logo">Tidy Lark<br>Cleaners</p>
      <p class="contact-name">Mona Pritchett</p>
      <div class="contact-lines">
        <p class="contact-phone">501-555-0147</p>
        <p class="contact-email">mona.pritchett@tidylarkmail.com</p>
      </div>
      <div class="back-figure" role="img" aria-label="Illustration of a 1950s pin-up maid holding a broom"></div>
    </div>
  </section>
</main>
</body>
</html>
```